Real Estate 2015 sold listings postcard

Real estate. I want one side to list 2015 sales. Mailing side with additional information. I am including a "concept" but it needs to be professionalized... Feel free to change color, fonts, layout, add watermark, whatever you think will work. Text on backside may be tweaked. I do want postcards addressed. How do i send mailing list or does Brightmark Press do that part?

NOTE: Postcard should be 8.5 x 5.5 inches.
Updates

postcard should be 8.5" x 5.5" size

Target Market(s)

Home owners who may want to sell

Industry/Entity Type

Real Estate Agent

Requirements
Must have
• The sold information and contact oinformation I have provided
Nice to have
• Watermark with my initials

```html
<!DOCTYPE html>
<html lang="en">
<head>
<meta charset="utf-8">
<title>2015 Sold Listings Postcard</title>
<link rel="stylesheet" href="https://fonts.googleapis.com/css2?family=Arimo:ital,wght@0,400;0,700;1,400;1,700&family=Cinzel:wght@400;700&family=Kaushan+Script&display=swap">
<style>
  :root {
    --red: #d0202e;
    --gold: #f2b81c;
    --gold-deep: #d9a514;
    --black: #231f20;
    --ink: #1a1a1a;
    --white: #ffffff;
    --paper-bg: #e4e4e2;
    --photo-a: #8c4a3a;
    --photo-b: #c8322f;
  }
  * { box-sizing: border-box; margin: 0; padding: 0; }
  html, body { width: 1200px; height: 1200px; overflow: hidden; }
  body { background: var(--paper-bg); font-family: "Arimo", Arial, sans-serif; color: var(--ink); position: relative; }

  .postcard { position: absolute; left: 180px; width: 840px; height: 544px; background: var(--white); overflow: hidden; box-shadow: 0 2px 8px rgba(0,0,0,.18); }
  .postcard--sales { top: 36px; }
  .postcard--mailing { top: 620px; }

  /* ---------- sales side ---------- */
  .sales-title { position: absolute; left: 50px; top: 18px; font-family: "Cinzel", Georgia, serif; font-size: 27px; letter-spacing: .5px; color: var(--ink); }
  .sales-title .year { color: var(--red); }
  .sold-stamp { position: absolute; left: 268px; top: 54px; padding: 1px 14px; border: 2px solid var(--red); color: var(--red); font-family: "Cinzel", Georgia, serif; font-weight: 700; font-size: 17px; letter-spacing: 3px; }
  .brand { position: absolute; display: flex; align-items: center; gap: 8px; font-family: "Cinzel", Georgia, serif; font-weight: 700; color: var(--ink); letter-spacing: 1px; }
  .brand__mark { width: 16px; height: 16px; background: var(--gold-deep); }
  .postcard--sales .brand { right: 50px; top: 46px; font-size: 19px; }

  .sales-table { position: absolute; left: 50px; top: 90px; width: 740px; border-collapse: collapse; table-layout: fixed; font-size: 10.5px; font-weight: 700; }
  .sales-table th { background: var(--red); color: var(--white); height: 19px; font-size: 10px; letter-spacing: .3px; border-top: 3px solid var(--black); }
  .sales-table td { background: var(--gold); height: 16px; border: 1px solid var(--black); text-align: center; padding: 0 3px; white-space: nowrap; }
  .sales-table td.addr { text-align: left; padding-left: 8px; }

  .agent-photo { position: absolute; border: 2px solid var(--white); outline: 1px solid var(--black); background: linear-gradient(160deg, var(--photo-a), var(--photo-b)); }
  .postcard--sales .agent-photo { left: 52px; top: 378px; width: 84px; height: 98px; }
  .side-stripe { position: absolute; left: 0; top: 412px; width: 50px; height: 24px; background: var(--red); }
  .agent-script { position: absolute; left: 156px; top: 374px; font-family: "Kaushan Script", cursive; color: var(--red); font-size: 34px; }
  .contact-row { position: absolute; left: 156px; top: 432px; display: flex; align-items: center; gap: 10px; font-size: 15px; }
  .contact-row .email-box { background: var(--red); color: var(--white); font-weight: 700; font-size: 17px; padding: 4px 12px; }
  .disclaimer { position: absolute; left: 156px; top: 474px; font-size: 8.5px; color: var(--ink); }
  .bottom-band { position: absolute; left: 20px; right: 20px; top: 492px; height: 34px; background: var(--red); color: var(--white); font-weight: 700; font-size: 19px; display: flex; align-items: center; justify-content: center; gap: 18px; }

  /* ---------- mailing side ---------- */
  .promo-panel { position: absolute; left: 0; top: 0; width: 590px; height: 336px; background: var(--black); color: var(--white); }
  .postcard--mailing .agent-photo { left: 24px; top: 22px; width: 88px; height: 98px; }
  .agent-name { position: absolute; left: 132px; top: 26px; font-weight: 700; font-size: 22px; color: var(--red); letter-spacing: .5px; }
  .agent-license { position: absolute; left: 132px; top: 54px; font-style: italic; font-size: 13px; color: var(--gold); }
  .agent-contact { position: absolute; left: 132px; display: flex; align-items: center; gap: 8px; }
  .agent-contact--phone { top: 78px; font-weight: 700; font-size: 16px; }
  .agent-contact--email { top: 100px; font-size: 15px; }
  .season-note { position: absolute; left: 24px; top: 142px; font-size: 16px; }
  .season-note em { font-weight: 700; }
  .benefits { position: absolute; left: 36px; top: 166px; list-style: none; font-weight: 700; font-size: 16px; }
  .benefits li { display: flex; align-items: center; gap: 8px; height: 21px; }
  .reach-note { position: absolute; left: 24px; top: 218px; font-size: 16px; }
  .reach-note strong { color: var(--gold); }
  .cta { position: absolute; left: 24px; top: 252px; font-weight: 700; font-size: 25px; }
  .cta .urgent { color: var(--red); margin-left: 6px; }
  .cta .tail { font-weight: 400; font-size: 17px; margin-left: 4px; }
  .cta-sub { position: absolute; left: 24px; top: 288px; font-size: 20px; color: var(--gold); }
  .market-copy { position: absolute; left: 0; top: 336px; width: 590px; height: 112px; background: var(--gold-deep); padding: 10px 20px; font-size: 10px; line-height: 1.32; color: var(--ink); }
  .postcard--mailing .brand { left: 612px; top: 36px; font-size: 19px; }
</style>
</head>
<body>

<section class="postcard postcard--sales" aria-label="Sales side">
  <h1 class="sales-title"><span class="year">2015</span> Sales in Your Neighborhood</h1>
  <div class="sold-stamp">SOLD</div>
  <div class="brand"><span class="brand__mark"></span>Harborline Realty</div>

  <table class="sales-table">
    <colgroup>
      <col style="width:170px"><col style="width:45px"><col style="width:50px"><col style="width:70px"><col style="width:80px"><col style="width:100px"><col style="width:100px"><col style="width:75px"><col style="width:50px">
    </colgroup>
    <thead>
      <tr><th>ADDRESS</th><th>BR</th><th>BA</th><th>SQ FT</th><th>LOT SIZE</th><th>LIST PRICE</th><th>SALE PRICE</th><th>$/SQ. FT</th><th>DOM</th></tr>
    </thead>
    <tbody>
      <tr><td class="addr">118 Alder PL</td><td>3</td><td>3 1/2</td><td>2588</td><td>9239</td><td>3088000</td><td>3,100,000</td><td>1198</td><td>9</td></tr>
      <tr><td class="addr">2415 Maple ST</td><td>4</td><td>3</td><td>2228</td><td>6147</td><td>2998000</td><td>3000000</td><td>1346</td><td>23</td></tr>
      <tr><td class="addr">205 Brookview DR</td><td>4</td><td>3</td><td>2185</td><td>7040</td><td>2800000</td><td>2925000</td><td>1339</td><td>9</td></tr>
      <tr><td class="addr">421 Lindell AVE*</td><td>3</td><td>2</td><td>1611</td><td>13 237</td><td>2498000</td><td>2610000</td><td>1620</td><td>8</td></tr>
      <tr><td class="addr">3908 Cedar AVE*</td><td>4</td><td>2</td><td>2297</td><td>8700</td><td>2250000</td><td>2595000</td><td>1130</td><td>8</td></tr>
      <tr><td class="addr">64 Hawthorn CIR</td><td>4</td><td>3</td><td>1364</td><td>5917</td><td>1788000</td><td>2475000</td><td>1815</td><td>8</td></tr>
      <tr><td class="addr">3521 Willow CIR</td><td>3</td><td>2</td><td>1646</td><td>6404</td><td>2500000</td><td>2475000</td><td>1504</td><td>8</td></tr>
      <tr><td class="addr">602 Mesa PL</td><td>3</td><td>2</td><td>1674</td><td>11200</td><td>2498000</td><td>2450000</td><td>1464</td><td>18</td></tr>
      <tr><td class="addr">247 Brookview DR*</td><td>4</td><td>2</td><td>1690</td><td>8178</td><td>2188000</td><td>2400000</td><td>1420</td><td>16</td></tr>
      <tr><td class="addr">319 Brookview DR</td><td>3</td><td>2</td><td>1674</td><td>8538</td><td>2200000</td><td>2260000</td><td>1350</td><td>7</td></tr>
      <tr><td class="addr">57 Hawthorn CIR</td><td>4</td><td>2</td><td>1543</td><td>6080</td><td>1488000</td><td>2250000</td><td>1458</td><td>97</td></tr>
      <tr><td class="addr">3766 Sutton CIR</td><td>3</td><td>2</td><td>1333</td><td>6493</td><td>1895000</td><td>2227500</td><td>1671</td><td>7</td></tr>
      <tr><td class="addr">388 Glenwood DR*</td><td>4</td><td>2</td><td>1740</td><td>6324</td><td>2200000</td><td>2180000</td><td>1253</td><td>6</td></tr>
      <tr><td class="addr">3519 Maple ST</td><td>3</td><td>2</td><td>1474</td><td>6111</td><td>1799000</td><td>2115000</td><td>1435</td><td>12</td></tr>
      <tr><td class="addr">48 Hawthorn Cir</td><td>2</td><td>2</td><td>1456</td><td>6111</td><td>1788000</td><td>2000000</td><td>1374</td><td>17</td></tr>
      <tr><td class="addr">216 Linden CT</td><td>2</td><td>2</td><td>1428</td><td>10,624</td><td>1,950,000</td><td>2,100,000</td><td>1471</td><td>20</td></tr>
    </tbody>
  </table>

  <div class="side-stripe"></div>
  <div class="agent-photo" role="img" aria-label="Portrait photo of the agent"></div>
  <div class="agent-script">Dana Whitfield</div>
  <div class="contact-row">
    <span class="email-box">dwhitfield@harborline.com</span>
    <span>| Relocation Specialist | California License #01234567</span>
  </div>
  <p class="disclaimer">* indicates Harborline Realty listing or sale. This information is deemed reliable, but not verified or guaranteed.</p>
  <div class="bottom-band"><span>650-555-0148</span><span>|</span><span>www.dwhitfieldhomes.com</span></div>
</section>

<section class="postcard postcard--mailing" aria-label="Mailing side">
  <div class="promo-panel">
    <div class="agent-photo" role="img" aria-label="Portrait photo of the agent"></div>
    <div class="agent-name">DANA WHITFIELD</div>
    <div class="agent-license">License: 01234567</div>
    <div class="agent-contact agent-contact--phone">
      <svg width="14" height="14" viewBox="0 0 14 14" aria-hidden="true"><rect width="14" height="14" rx="2" fill="var(--gold)"/><path d="M4 3.5c.6-.5 1.2-.4 1.5.2l.6 1.2c.2.4 0 .8-.3 1l-.5.4c.4.9 1 1.6 1.9 2l.4-.5c.3-.3.7-.4 1-.2l1.2.6c.6.3.7.9.2 1.5-.8.9-2 .9-3.4 0S4.3 7.6 3.6 6.1c-.5-1.1-.3-2 .4-2.6z" fill="var(--black)"/></svg>
      <span>650-555-0148</span>
    </div>
    <div class="agent-contact agent-contact--email">
      <svg width="14" height="11" viewBox="0 0 14 11" aria-hidden="true"><rect x=".6" y=".6" width="12.8" height="9.8" fill="none" stroke="var(--gold)" stroke-width="1.2"/><path d="M1 1l6 5 6-5" fill="none" stroke="var(--gold)" stroke-width="1.2"/></svg>
      <span>dwhitfield@harborline.com</span>
    </div>

    <p class="season-note">Traditionally, <em>Feb through April</em> are the best months to sell</p>
    <ul class="benefits">
      <li><svg width="14" height="12" viewBox="0 0 14 12" aria-hidden="true"><path d="M1 6l4 4 8-9" fill="none" stroke="var(--gold)" stroke-width="2.6"/></svg>Most Offers</li>
      <li><svg width="14" height="12" viewBox="0 0 14 12" aria-hidden="true"><path d="M1 6l4 4 8-9" fill="none" stroke="var(--gold)" stroke-width="2.6"/></svg>Highest prices</li>
    </ul>
    <p class="reach-note">Our Listings are advertised locally and in <strong>40 countries!!</strong></p>
    <p class="cta">Don't Wait!<span class="urgent">CALL NOW!</span><span class="tail">for a</span></p>
    <p class="cta-sub">PRIVATE CONSULTATION!</p>
  </div>
  <p class="market-copy">Our market continues to be strong, which reflects both our vibrant and growing local economy and our steady shortage of inventory. As long as those conditions continue, our market values will remain high. That is good news for sellers who may want to down-size or move to a different area for a new job, or maybe to be closer to family. I am a certified Relocation Specialist, and as such, I can connect you with experienced and professional agents almost anywhere in the country and in most countries around the world. We can coordinate your transactions at both ends, making your transition as seamless as possible. If you are planning a move, across the street or across the county, call me now for a confidential consultation.</p>
  <div class="brand"><span class="brand__mark"></span>Harborline Realty</div>
</section>

</body>
</html>
```